Ridgeline Throttle Touring Company needs brochure

We need a brochure for our motorcycle tour company, we run tours and provide other services like day rides, bespoke trips, heli taxis, trekking, mountain biking, white water rafting etc. We are a small company that runs the tours ourselves, providing excellent customer service . We are team of international friendly motorcycle enthusiasts with a passion for Nepal. With an office in the UK and in Nepal. Our brochure should reflect quality adventures, showcasing the Nepal Himalayas, our tours, and shout adventure. Target audience are Adventure Bikers. Below are some photos (all of which are owned by us, for use on our brochure only) Also the document with all the content for the brochure.

Target Market(s)

Adventure Motorbike Riders

Industry/Entity Type

Travel

Other font styles liked:
• Aurora for headings...

Requirements
Must have
• Adventure Feel. Looking cool and modern. Well thought out colour palette. Include big photos. Sometimes as background to text.
• touring in the himalayas:
Nice to have
• Infographics for the include exclude section.
• Want it to be A5 brochure, landscape, probably be needing 14 pages. Might make it shorter to 12 if possible.
• If you have access to vectors/graphics please use stuff related to Nepal like Buddhas eyes, stupas, prayer flags, bells, shiva trident, mountains, tyre tracks etc. Be imaginative and creative. I have uploaded a photo of rough layout but is quite open to interpretation. Need photos and text to be clear. Please let me know if any photos are not good quality.
Should not have
• It shouldn't look like a corporate brochure, boring,
• It shouldn't look like a Brokker Vantell type trip. We use adventure bikes.

```html
<!DOCTYPE html>
<html lang="en">
<head>
<meta charset="utf-8">
<title>Ridgeline Throttle – Brochure Spreads</title>
<link href="https://fonts.googleapis.com/css2?family=Barlow+Condensed:wght@500;600;700&family=Barlow+Semi+Condensed:wght@400;600&family=Russo+One&display=swap" rel="stylesheet">
<style>
:root{
  --bg:#e9eaec;
  --red:#e2231a;
  --deep-red:#8e1412;
  --coral:#ea6a52;
  --navy:#2b2f7e;
  --blue:#1f5fae;
  --grey:#8b8b8d;
  --ink:#2a2a33;
  --white:#ffffff;
  --peach:#f6d3c4;
}
*{margin:0;padding:0;box-sizing:border-box}
html,body{width:1086px;height:1200px;overflow:hidden;background:var(--bg)}
body{position:relative;font-family:"Barlow Semi Condensed",sans-serif;color:var(--ink)}
.spread{position:absolute;left:106px;width:875px;height:308px;background:var(--white);overflow:hidden;box-shadow:4px 5px 10px rgba(0,0,0,.28)}
.spread--cover{top:106px}
.spread--about{top:446px}
.spread--services{top:786px}
.spread svg.art{position:absolute;inset:0}
.block{position:absolute;font-size:6px;line-height:8.6px}
.block p{margin-bottom:6px}
.justify{text-align:justify}
.right{text-align:right}
.on-dark{color:var(--white)}
.heading{font-family:"Barlow Condensed",sans-serif;font-weight:600;font-size:14px;line-height:16px;position:relative;display:inline-block;padding-bottom:6px;margin-bottom:8px}
.heading::after{content:"";position:absolute;left:0;bottom:0;width:100%;height:1px;background:currentColor}
.heading::before{content:"";position:absolute;right:-2px;bottom:-2px;width:5px;height:5px;border-radius:50%;background:currentColor}
.heading--navy{color:var(--navy)}
.heading--navy::after,.heading--navy::before{background:var(--red)}
.sub{font-family:"Barlow Condensed",sans-serif;font-weight:600;font-size:9px;line-height:11px;color:var(--white);font-style:italic}
.contact{font-family:"Barlow Condensed",sans-serif;font-weight:600;font-size:8px;line-height:10.5px;font-style:italic}
.brand{position:absolute;display:flex;align-items:center;gap:4px;font-family:"Barlow Condensed",sans-serif;font-weight:700;font-size:10px;letter-spacing:.5px}
.brand i{display:block;width:12px;height:12px;border-radius:50%;background:var(--red)}
.title{position:absolute;right:18px;top:46px;text-align:right;font-family:"Russo One",sans-serif;color:var(--red);font-size:17px;line-height:21.5px}
.services p{margin-bottom:8px;font-size:6.2px}
.partner{position:absolute;left:454px;top:212px;font-family:"Barlow Condensed",sans-serif;font-weight:700;font-size:36px;line-height:36px;color:#f2c200;letter-spacing:1px}
</style>
</head>
<body>

<!-- Spread 1: back and front cover -->
<section class="spread spread--cover">
  <svg class="art" width="875" height="308" viewBox="0 0 875 308">
    <defs>
      <linearGradient id="redPeak" x1="0" y1="0" x2="1" y2="1">
        <stop offset="0" stop-color="#c8231d"/><stop offset=".6" stop-color="#e2231a"/><stop offset="1" stop-color="#9b1512"/>
      </linearGradient>
      <linearGradient id="trailPhoto" x1="0" y1="0" x2="0" y2="1">
        <stop offset="0" stop-color="#4f6a3a"/><stop offset=".55" stop-color="#7c7a55"/><stop offset="1" stop-color="#b8a98a"/>
      </linearGradient>
      <linearGradient id="summitPhoto" x1="0" y1="0" x2="0" y2="1">
        <stop offset="0" stop-color="#9fb4cf"/><stop offset=".35" stop-color="#d9dde3"/><stop offset=".55" stop-color="#7b6a5c"/><stop offset="1" stop-color="#a48d76"/>
      </linearGradient>
      <pattern id="stripes" width="14" height="14" patternUnits="userSpaceOnUse" patternTransform="rotate(45)">
        <line x1="0" y1="0" x2="0" y2="14" stroke="#ececef" stroke-width="4"/>
      </pattern>
    </defs>
    <polygon points="0,160 0,308 150,308 82,228" fill="var(--grey)"/>
    <polygon role="img" aria-label="Red-tinted photo of Himalayan peaks" points="134,0 438,0 438,308 36,308" fill="url(#redPeak)"/>
    <polygon points="100,0 140,0 256,116 236,136" fill="var(--coral)" opacity=".85"/>
    <polyline points="205,40 292,126 205,212" fill="none" stroke="var(--white)" stroke-width="2" opacity=".6"/>
    <polygon role="img" aria-label="Photo of a rider with an adventure motorcycle on a forest trail" points="126,34 218,126 126,218 34,126" fill="url(#trailPhoto)" stroke="var(--white)" stroke-width="3"/>
    <polygon points="58,164 76,182 58,200 40,182" fill="var(--coral)"/>
    <polygon points="82,186 114,218 82,250 50,218" fill="var(--navy)"/>
    <text transform="translate(196,205) rotate(-45)" text-anchor="middle" font-family="Barlow Condensed, sans-serif" font-weight="700" font-size="17" fill="#fff">www.ridgelinethrottle.co.uk</text>
    <ellipse role="img" aria-label="Map of Europe and Asia linking the UK and Nepal" cx="365" cy="100" rx="49" ry="30" fill="#bdbdbf"/>

    <rect x="438" y="0" width="437" height="308" fill="url(#stripes)"/>
    <polygon role="img" aria-label="Photo of a rider celebrating beside a motorcycle below snowy Himalayan peaks" points="438,0 668,0 618,158 700,308 438,308" fill="url(#summitPhoto)"/>
    <polygon points="438,45 452,60 438,75" fill="var(--navy)"/>
    <polygon points="775,0 835,0 678,158 835,308 775,308 618,158" fill="var(--red)" opacity=".78"/>
    <line x1="830" y1="0" x2="680" y2="150" stroke="var(--coral)" stroke-width="5"/>
    <polygon points="690,185 740,135 875,270 875,308 812,308" fill="var(--grey)"/>
    <text transform="translate(790,240) rotate(45)" text-anchor="middle" font-family="Barlow Condensed, sans-serif" font-weight="700" font-size="17" fill="#fff">www.ridgelinethrottle.co.uk</text>
  </svg>

  <div class="brand" style="left:16px;top:40px;color:var(--navy)"><i></i>RIDGELINE THROTTLE</div>
  <div class="brand" style="left:470px;top:40px;color:var(--white)"><i></i>RIDGELINE THROTTLE</div>

  <div class="block right on-dark" style="left:270px;top:26px;width:150px">
    <div class="sub">Where to Find Us?</div>
    <p>With one foot in the UK and one foot in Nepal, we are ideally placed to organise your Himalayan adventures.</p>
  </div>
  <div class="block right on-dark" style="left:280px;top:143px;width:140px;font-size:5px;line-height:7px">
    <p>Got a dream of travelling to the Himalayas? I'll be your first contact right here in the UK to answer any questions about travelling to Nepal or Tibet. Don't hesitate to reach me via email or directly on my mobile.</p>
  </div>
  <div class="block right on-dark" style="left:230px;top:178px;width:190px">
    <div class="contact">Looking forward to hearing from you!<br>Mara<br>Mobile/ Whatsapp: (+44)07700 900512<br>Email: mara@ridgelinethrottle.co.uk</div>
  </div>
  <div class="block right on-dark" style="left:180px;top:226px;width:240px;font-size:4.6px;line-height:6.4px">
    <div class="sub" style="margin-bottom:2px">Already in Kathmandu?</div>
    <p style="margin-bottom:2px">Come visit us at our office in Lakeside Bazaar, Kathmandu. You can rent one of our bikes for your own self guided tour or book a guided day ride if you want to experience the Himalayas by motorcycle but don't have much time.</p>
    <p style="margin-bottom:2px;font-weight:600;font-style:italic">Kenji or Arjun will be there to assist you.<br>Mobile: (+977)9800 000112 Office: (+977)01 5550140</p>
    <p>Check out our website for more details or find us on our social channels, like, follow and subscribe to our pages for all our news and updates.</p>
  </div>

  <div class="title">THE<br>ULTIMATE<br>HIMALAYAN<br>MOTORCYCLE<br>ADVENTURE</div>
</section>

<!-- Spread 2: about us, social work, touring -->
<section class="spread spread--about">
  <svg class="art" width="875" height="308" viewBox="0 0 875 308">
    <defs>
      <linearGradient id="duskRange" x1="0" y1="0" x2="1" y2="0.4">
        <stop offset="0" stop-color="#4a1a1d"/><stop offset=".55" stop-color="#a81d1f"/><stop offset="1" stop-color="#e2231a"/>
      </linearGradient>
      <linearGradient id="valleyShade" x1="0" y1="0" x2="0" y2="1">
        <stop offset=".5" stop-color="#000" stop-opacity="0"/><stop offset="1" stop-color="#3a0c0e" stop-opacity=".7"/>
      </linearGradient>
    </defs>
    <rect role="img" aria-label="Red-toned photo of misty mountain ridges" x="0" y="0" width="598" height="308" fill="url(#duskRange)"/>
    <rect x="0" y="0" width="598" height="308" fill="url(#valleyShade)"/>
    <polygon points="598,296 700,284 875,300 875,308 598,308" fill="var(--navy)"/>
    <polygon points="598,291 700,282 760,287 700,286 598,296" fill="var(--red)"/>
    <polygon points="760,292 875,286 875,300" fill="var(--blue)"/>
  </svg>

  <div class="block on-dark" style="left:33px;top:36px;width:380px">
    <div class="heading">About Us</div>
    <p>Here at Ridgeline Throttle we are the creators and the providers of all our motorcycle tours.</p>
    <p>With a life-time of experience behind us with riding the roads in the Himalayas our unique motorcycle trips will show you the world's tallest peaks, take you over the other side of the Himalayas into Tibet, explore the tropical southern flatlands, home of the Royal Bengal Tiger and bring you to the birthplace of Buddha.</p>
    <p>We have a fleet of Torvane TR250s, these bikes are light an agile, with a good handful of torque when you need it, perfectly suited to the mountainous terrain. And they are all fitted with ABS plus a digital dash.</p>
    <p>Anyone is welcome to sign up to one of our Himalayan motorcycle adventures, no matter what gender, age, ethnicity or belief.</p>
  </div>
  <div class="block on-dark" style="left:33px;top:161px;width:180px">
    <div class="heading">Social Work</div>
    <p class="justify">Each trip we run helps provide funds for our social projects in Nepal. We currently give to the Sunrise Valley Science Scholarship Fund, which provides outstanding students from Sindhuli District with tuition and maintenance fees for university in Nepal. Sindhuli District is close to our hearts and we all would like to see this part of Nepal develop and flourish. The scholarship fund is one of the best ways to give young students a chance for further education.</p>
  </div>
  <div class="block on-dark justify" style="left:230px;top:190px;width:180px">
    <p>Arjun (pic): With many journeys both on motorbike and on foot with his friends, colleagues and clients across Nepal, travel and adventure are in his blood. Arjun's military background makes it possible to provide personal welcomes across the country and also handle with ease any problems met with on the challenging terrain. He is a huge asset to the team and puts his heart and soul into everything he does, so you can rely on him to make your Himalayan adventure the most epic it could be.</p>
  </div>
  <div class="block on-dark justify" style="left:454px;top:36px;width:124px">
    <div class="heading">Social Work</div>
    <p>Mara (pic) will travel with you to make sure your experience is unforgettable. Coming from a background in Public Health, Mara has lived in Peru, Spain, the Netherlands and Nepal. She is from the UK and was educated at an international university in Europe. As well as working to make your trip to Nepal a great experience, she is your first contact in the UK for help with flight tickets, visas, vaccinations (or simply what to pack!) via phone or email.</p>
    <p style="margin-top:10px">Kenji (pic): With 30 years of work in the tourism industry he brings a lot of experience to the team. Having a keen sense for detail his mechanical abilities often save the day and when not on a motorbike he's driving the support vehicle like a pro. Always friendly and easy-going he's great company and has a depth of technical knowledge about Nepal ranging from its architecture to its helicopters!</p>
  </div>
  <div class="block justify" style="left:614px;top:36px;width:235px">
    <div style="text-align:right"><div class="heading heading--navy">Touring in the HIMALAYAS</div></div>
    <p>Nepal is a country that descends from the Rooftop of the World, Tibet, encompassing within it the 8 highest peaks of the world (including Mount Everest) that extend southwards towards the gigantic plain of India. With giant Himalayan rivers that offer unique natural beauty. It is home to countless Hindu deities, the birthplace of Buddha, the legendary Yeti, 61 ethnic tribes with different dialects and cultures. Many species of endangered and exotic animals, birds, plants and trees, including one-horned Rhinos, Musk-deer, Bengal tigers, White leopards, Dolphins, Pandas, Wild Buffalos, Wild Elephants, Himalayan Yaks, special Aardvark, Golden Eagle, migrating Siberian Goose, wild orchids and native Rhododendron Trees amongst much more.</p>
    <p style="margin-top:10px">It offers countless lofty and spiritual peaks, lakes, ancient Hindu shrines and temples, Buddhist monasteries and lost valleys including camps of indigenous hunting and gathering people, mobile camps of Tibetan Shepherds, and communities of Honey Hunters. The adventures are endless and amazement is around every bend.</p>
    <p style="margin-top:10px">Tiny villages to urban cities scattered throughout the country are divided largely by the soaring and mystic mountains, hills, roaring and twisting serpentine rivers and streams. They offer different, unique and vibrant cultures, dialects, climates, culinary cuisines, architecture, flora and fauna providing colourful contrasts to each other. Riding and traveling around this small country brings constant changes in vista, dweller, tests, experience and atmosphere to the never ending amusement of the bewildered traveller.</p>
  </div>
</section>

<!-- Spread 3: on the road, our services -->
<section class="spread spread--services">
  <svg class="art" width="875" height="308" viewBox="0 0 875 308">
    <defs>
      <linearGradient id="nightRange" x1="0" y1="0" x2="0" y2="1">
        <stop offset="0" stop-color="#26296e"/><stop offset=".7" stop-color="#2f3384"/><stop offset="1" stop-color="#5b5fa6"/>
      </linearGradient>
      <linearGradient id="shrineFigure" x1="0" y1="0" x2="1" y2="1">
        <stop offset="0" stop-color="#c8462e"/><stop offset=".5" stop-color="#3a3636"/><stop offset="1" stop-color="#b98a3e"/>
      </linearGradient>
    </defs>
    <rect role="img" aria-label="Deep blue photo of mountain silhouettes" x="0" y="0" width="438" height="308" fill="url(#nightRange)"/>
    <polygon points="560,308 845,140 865,308" fill="var(--peach)" opacity=".75"/>
    <polygon points="820,40 875,0 875,308 830,308" fill="#2f3443"/>
    <polygon points="755,15 771,31 755,47 739,31" fill="var(--coral)"/>
    <polygon points="845,30 861,46 845,62 829,46" fill="var(--coral)" opacity=".8"/>
    <polygon role="img" aria-label="Photo of a painted Nepali temple deity statue" points="700,130 770,60 840,130 875,110 875,250 800,290 730,240" fill="url(#shrineFigure)"/>
    <polygon points="790,120 825,155 790,190 755,155" fill="var(--navy)"/>
    <polygon points="860,200 875,215 860,230 845,215" fill="var(--coral)"/>
    <polygon points="690,250 705,265 690,280 675,265" fill="#9c8fc8"/>
    <polygon points="704,262 716,274 704,286 692,274" fill="#6a5fa8"/>
    <polygon points="438,292 560,282 700,296 875,290 875,308 438,308" fill="var(--blue)"/>
    <polygon points="438,299 600,292 875,302 875,308 438,308" fill="var(--navy)"/>
    <polygon points="0,290 120,280 260,296 438,286 438,308 0,308" fill="#4b4f96" opacity=".6"/>
  </svg>

  <div class="block on-dark justify" style="left:28px;top:30px;width:382px">
    <p>Tiny villages to urban cities scattered throughout the the country are divided largely by the soaring and mystic mountains, hills, roaring and twisting serpentine rivers and streams. They offer different, unique and vibrant cultures, dialects, climates, culinary cuisines, architecture, flora and fauna providing colourful contrasts to each other. Riding and traveling around this small country brings constant changes in vista, dweller, tests, experience and atmosphere to the never ending amusement of the bewildered traveller.</p>
    <p>Driving in Nepal is on the left side, as in the UK. There are many hazards to be aware of whilst riding in Nepal. The road conditions are different wherever you go. The roads can suddenly change from smooth black top to bumpy dirt without any signage or notice. There are no notice signs for hazards, obstacles or anything else so be aware and careful of, such as pot holes, mud holes, dirt patches, speed breakers, ditches, cracks, oil slicks, sand, water and streams. There are many temporary and permanent settlements on the side of the road and on the road with people, children and livestock. The road or highway is also used as a sidewalk and sometimes the front yard, so there will be people walking, sunbathing and chatting. Near the settlements you have to be aware and careful of: children playing, children going to school, adults, dogs, chickens, ducks, goats, cows, buffaloes, bicycles and people under the influence of alcohol. You will have to be aware and careful of other vehicles on the road. People, bicycles, motorcycles, scooters, tractors, rickshaws, buffalo carts, cows, elephants, cars, pickups, buses and trucks all use the road. Most of our tours travel on roads with relatively less traffic, there will always be a guide at the front and a sweeper at the back, with the support vehicle behind them for most of the way. We travel slowly as a group and always in single file, road safety is paramount in Nepal considering the risks are higher riding on mountainous roads. No racing or aggressive riding is accepted on our tours.</p>
    <p>Accommodation in Nepal ranges from 5* resorts to small teahouses. On our tours we try to use the best available accommodation where possible as after a hard days ride, it's great to chill out in comfort. However outside of the major cities options can be limited. Our itineraries include a wide range of accommodation including riverside resorts, hilltop hotels, jungle lodges, idyllic peninsula hideaways, teahouses and sometimes even camping. Whilst the itinerary says camping, all you need to do is show up, the rest is taken care of. Although we only stay in teahouses or camp when there really is no other option, each tour's accommodation is different as we travel to different regions of Nepal, some tours are all hotels whereas others are predominantly teahouses or a mixture of the two.</p>
    <p>Nepalis live on a staple diet of rice, lentil soup and veggies, the famous Dal Bhat. Outside of major cities this will be the main thing on the menu. Meat is also widely available, often either mutton, buffalo or yak meat, and sometimes chicken. In Kathmandu and Pokhara you can find all types of international cuisine.</p>
  </div>

  <div class="block services" style="left:454px;top:30px;width:200px">
    <div class="heading heading--navy">Our Services</div>
    <p>Guided Motorcycle Tours around Nepal and Tibet</p>
    <p style="margin-bottom:14px">Day Rides around Kathmandu valley</p>
    <p>Bespoke Motorcycle trips; Include white water rafting, trekking, paragliding, mountain biking, bungee jump, zip line, safari, jeep tour, heli tour or whatever interests you.</p>
    <p>Heli Taxis, for those short on time, quickly access popular trekking routes or unspoilt remote destinations</p>
    <p>Plus Yoga courses, photography, art and writing retreats...</p>
  </div>
  <div class="block" style="left:454px;top:194px;width:120px;font-size:6px">All protected with</div>
  <div class="partner">SAFEPATH</div>
</section>

</body>
</html>
```